Style Template created - Report Accounting and Advisory industry

We need a style template created to set out a report for advice. The report follows <br/><br/>- Cover Page - ( we would need to print to a letter head )<br/>- General Disclaimer<br/>- Space to add Excel Reports in to the document- Maybe inserted Pdf's later<br/>- Action Plan dot points under headings<br/>- List of Strategies to be adopted<br/><br/>Attached is a quick example word doc that needs Custom Style Templates made so that we can quickly format items added. Also the ugly PDF that we currently produce for clients <br/><br/>Red - is our preferred Colour<br/><br/>

Target Market(s)

Accounting / Business / Professionals

Industry/Entity Type

Accounting

Colors
ec1f27

Requirements
Nice to have
• Simple Clean design. Not to busy. Easy to modify the "wording text" in design
Should not have
• Too busy or too much color

```html
<!DOCTYPE html>
<html lang="en">
<head>
<meta charset="utf-8">
<title>Taxation Projection and Planning 2020 – Report Template</title>
<link href="https://fonts.googleapis.com/css2?family=Open+Sans:wght@300;400;600;700&family=Arimo:wght@400;700&display=swap" rel="stylesheet">
<style>
  :root{
    --red:#b5121b;
    --red-bright:#ec1f27;
    --ink:#333333;
    --grey-band:#6d6e71;
    --grey-soft:#f1f1f1;
    --row-shade:#f0f0f0;
    --backdrop:#1b1b1b;
    --paper:#ffffff;
  }
  *{box-sizing:border-box;margin:0;padding:0}
  html,body{width:1200px;height:1200px;overflow:hidden;background:var(--backdrop)}
  body{position:relative;font-family:"Arimo",Arial,sans-serif;color:var(--ink)}

  .page{position:absolute;width:360px;height:509px;background:var(--paper);overflow:hidden}
  .page--cover{left:225px;top:72px}
  .page--disclaimer{left:615px;top:72px}
  .page--intro{left:225px;top:619px}
  .page--figures{left:615px;top:619px}

  /* brand name */
  .brand{font-family:"Open Sans",sans-serif;font-weight:400;color:var(--red);letter-spacing:.02em;line-height:1;white-space:nowrap}
  .brand-tag{font-family:"Open Sans",sans-serif;color:#8a8a8a;text-transform:uppercase;letter-spacing:.04em}

  /* cover */
  .cover-wedge{position:absolute;left:0;top:0}
  .cover-brand{position:absolute;left:35px;top:36px}
  .cover-brand .brand{font-size:17px}
  .cover-brand .brand-tag{font-size:5.5px;margin-top:3px}
  .cover-seal{position:absolute;left:277px;top:22px;width:42px;height:42px;border-radius:50%;background:radial-gradient(circle at 40% 35%,#c8202a,#8e0d14)}
  .cover-title{position:absolute;left:95px;top:130px;font-family:"Open Sans",sans-serif}
  .cover-title .lead{display:block;font-size:22px;font-weight:700;color:var(--red);line-height:1}
  .cover-title .rest{display:block;font-size:30px;font-weight:300;color:var(--ink);line-height:32px;margin-top:2px}
  .cover-client{position:absolute;left:95px;top:264px;font-family:"Arimo",sans-serif;font-weight:700;font-size:10px;color:#444}
  .cover-photo{position:absolute;left:0;top:245px;width:360px;height:196px;background:linear-gradient(180deg,#ffffff 0%,#ece9e4 30%,#c9c4bb 65%,#d9d6d0 100%)}
  .cover-band{position:absolute;left:0;top:441px;width:360px;height:68px;background:var(--red)}
  .cover-url{position:absolute;right:33px;bottom:22px;font-family:"Open Sans",sans-serif;font-weight:700;font-size:8px;color:#fff}

  /* inner page chrome */
  .page-head{position:absolute;left:34px;top:18px;width:292px;height:16px;border-bottom:.6px solid var(--red)}
  .page-head .brand{font-size:11px}
  .page-head .brand-tag{font-size:3.4px;margin-top:1px}
  .page-head-meta{position:absolute;right:0;bottom:1.5px;font-family:"Open Sans",sans-serif;font-size:3.8px;color:#666}
  .page-head-meta b{color:#222;font-weight:700}
  .page-foot{position:absolute;left:0;top:481px;width:360px;height:16px}
  .page-foot-copy{position:absolute;left:34px;top:5px;font-family:"Open Sans",sans-serif;font-size:4.3px;color:#fff}
  .page-foot-num{position:absolute;right:14px;top:4px;font-family:"Open Sans",sans-serif;font-weight:700;font-size:6px;color:#fff}

  /* body text */
  .copy{position:absolute;left:34px;width:292px;font-size:6.1px;line-height:7.4px;color:#333}
  .copy p{margin-bottom:7px}
  .copy strong{font-weight:700}

  .disclaimer-title{position:absolute;left:0;width:360px;top:110px;text-align:center;font-weight:700;font-size:10.5px;color:#333}
  .signoff{position:absolute;left:34px;top:422px;font-size:6.1px;line-height:7.4px}

  .section-title{font-weight:700;font-size:9.4px;color:var(--red);margin:8px 0 2px;letter-spacing:.01em}
  .section-title:first-child{margin-top:0}
  .benefits{list-style:none;margin:0 0 6px}
  .benefits li{padding-left:9px;position:relative}
  .benefits li::before{content:"";position:absolute;left:1px;top:2.6px;width:2.3px;height:2.3px;background:#333}

  /* figures table */
  .fig-title{position:absolute;left:34px;top:74px;font-family:"Open Sans",sans-serif;font-size:8px;line-height:15.5px;color:#222}
  .fig-currency{position:absolute;left:287px;top:92px;font-family:"Open Sans",sans-serif;font-size:4.6px;font-weight:700}
  .fig-table{position:absolute;left:31px;top:105px;width:295px;border-collapse:collapse;font-family:"Open Sans",sans-serif;font-size:5px;color:#222}
  .fig-table td{height:17.3px;padding:0 3px}
  .fig-table tr:nth-child(odd) td{background:var(--row-shade)}
  .fig-table tr.blank td{background:none}
  .fig-table td.val{width:75px;text-align:center}
  .fig-table td.val.rule{border-bottom:.6px solid #444}
  .u{text-decoration:underline}
  .fig-total{position:absolute;left:31px;top:465px;width:295px;height:0;border-top:.7px solid #222}
  .fig-total-row{position:absolute;left:31px;top:447px;width:295px;height:17px;display:flex;align-items:center;justify-content:space-between;padding:0 18px 0 3px;font-family:"Open Sans",sans-serif;font-weight:700;font-size:5px;color:#111}
  .fig-total-row .num{font-size:6px}
  .fig-total-top{position:absolute;left:31px;top:446px;width:295px;border-top:.7px solid #222}
</style>
</head>
<body>

<!-- Cover -->
<section class="page page--cover">
  <svg class="cover-wedge" width="261" height="180" viewBox="0 0 261 180"><polygon points="0,0 261,0 0,180" fill="#f1f1f1"/></svg>
  <div class="cover-brand">
    <div class="brand">HALLETT REEVE</div>
    <div class="brand-tag">Chartered Accountants</div>
  </div>
  <div class="cover-seal" role="img" aria-label="Red wax seal decoration"></div>
  <h1 class="cover-title">
    <span class="lead">TAXATION</span>
    <span class="rest">PROJECTION<br>AND PLANNING<br>2020</span>
  </h1>
  <div class="cover-photo" role="img" aria-label="Soft-focus photo of a business meeting around an office table with glasses and pen"></div>
  <div class="cover-client">Client Name</div>
  <div class="cover-band"><span class="cover-url">www.hallettreeve.com.au</span></div>
</section>

<!-- Disclaimer -->
<section class="page page--disclaimer">
  <header class="page-head">
    <div class="brand">HALLETT REEVE</div>
    <div class="brand-tag">Chartered Accountants</div>
    <div class="page-head-meta">2019 Tax Planning | <b>Summit Crane Rentals Pty Ltd</b></div>
  </header>
  <h2 class="disclaimer-title">DISCLAIMER</h2>
  <div class="copy" style="top:141px">
    <p>The taxation estimate has been prepared on the basis of information provided by the client. The report Is intended for internal tax planning purposes and represents a "What if scenario". It does not necessarily represent real or intended transactions.</p>
    <p>HallettReeve have not performed any tests to verify or validate any of the information provided by the client and accordingly express no assurance as to the outcome indicated.</p>
    <p>To the extent permitted by law we do not accept liability for any loss or damage which any person, other than the client may suffer arising from any negligence on our part. No person should rely on the Taxation estimate without having a full review or audit conducted on the data.</p>
    <p style="margin-bottom:0"><strong>Superannuation</strong><br>Provision of Advice is guided by legislative requirements to be provided in a Statement of Advice. Any and all comments regarding Superannuation are not to be taken as advice rather than statement of factual information about the situation. The statement is not a recommendation to take any action unless that action is required by law. The clients personal situation has not been considered in</p>
    <p style="margin-top:7px">providing the information. Any action to be taken in relation to the information provided, should take into account the clients personal situation and consideration must be given as to whether action will be appropriate for the clients' objectives and needs. Specific Contribution amounts and SMSF product advice can only be provided under a Statement of Advice by a AFSL Holder.</p>
  </div>
  <div class="signoff"><strong>HallettReeve</strong><br>Chartered Accountants</div>
  <footer class="page-foot">
    <svg width="360" height="16" viewBox="0 0 360 16" style="position:absolute;left:0;top:0"><rect width="360" height="16" fill="#6d6e71"/><polygon points="318,0 360,0 360,16 306,16" fill="#ffffff"/><polygon points="321,0 360,0 360,16 310,16" fill="#b5121b"/></svg>
    <span class="page-foot-copy">© 2020 HallettReeve Chartered Accountants</span>
    <span class="page-foot-num">2</span>
  </footer>
</section>

<!-- Introduction -->
<section class="page page--intro">
  <header class="page-head">
    <div class="brand">HALLETT REEVE</div>
    <div class="brand-tag">Chartered Accountants</div>
    <div class="page-head-meta">2019 Tax Planning | <b>Summit Crane Rentals Pty Ltd</b></div>
  </header>
  <div class="copy" style="top:55px">
    <h3 class="section-title">INTRODUCTION</h3>
    <p>Tax planning is the activities taken to minimise tax liabilities to ensure all available allowances, deductions, exclusions and exemptions are working together in the most tax effective manner to reduce the total tax bill.</p>
    <h3 class="section-title">IMPORTANCE</h3>
    <p>Tax planning strategies are typically employed to help a business achieve their financial and business goals.</p>
    <p style="margin-bottom:1px">The benefits of tax planning are:</p>
    <ul class="benefits">
      <li>Lowering the amount of taxable income</li>
      <li>Reducing the tax rate</li>
      <li>Allowing greater control of when taxes get paid</li>
      <li>Better management of your cash flow</li>
      <li>Eliminating nasty tax surprises</li>
    </ul>
    <h3 class="section-title">ESTIMATED TAX POSITION</h3>
    <p>We have reviewed your projected financial position for the period 1 July 2018 to 30 June 2019, and we have outlined below recommendations to legally reduce your tax. The recommendations and estimated tax positions we have outlined in this report reflect the tax laws that are current as at the date of this report.</p>
    <p>We estimate that you will save $19,800 of tax if you implement all of our recommendations before 30 June 2019. After implementing these strategies, we estimate your marginal tax rate on your income to be 27.5%</p>
    <h3 class="section-title">BACKGROUND TO TAX PLANNING</h3>
    <p>Everyone wants to increase their tax refund (or reduce their tax payable). We're here to help you to do this! Tax saving recommendations generally involve you spending money on "something" which creates for you a tax deduction. The "something" you spend your money on could be an expense, an asset, or an investment related payment (like superannuation or prepaid interest on an investment loan).</p>
    <p>However – please don't fall into a common trap of spending money just to get a tax deduction. You only save tax based on the marginal tax rate proportion on the amount you spend, not the full amount you spend. For example, to save tax, you generally need to spend money. If you earn $90,000 and your marginal tax rate is 39%, this means that if you spend $100 to get a tax deduction, you then get $39 back as a tax deduction, and you have spent $61 to buy the tax deduction.</p>
    <h3 class="section-title">OUR RECOMMENDATIONS</h3>
    <p>The purpose of this report is to provide a recommendation of tax saving strategies for you to consider for the2019 tax year. This report is not intended to be our final advice to you, but instead is a starting point in educating you on some potential opportunities for you to maximise your tax savings for the current 2019 year.</p>
  </div>
  <footer class="page-foot">
    <svg width="360" height="16" viewBox="0 0 360 16" style="position:absolute;left:0;top:0"><rect width="360" height="16" fill="#6d6e71"/><polygon points="318,0 360,0 360,16 306,16" fill="#ffffff"/><polygon points="321,0 360,0 360,16 310,16" fill="#b5121b"/></svg>
    <span class="page-foot-copy">© 2020 HallettReeve Chartered Accountants</span>
    <span class="page-foot-num">3</span>
  </footer>
</section>

<!-- Figures -->
<section class="page page--figures">
  <header class="page-head">
    <div class="brand">HALLETT REEVE</div>
    <div class="brand-tag">Chartered Accountants</div>
    <div class="page-head-meta">2019 Tax Planning | <b>Summit Crane Rentals Pty Ltd</b></div>
  </header>
  <div class="fig-title">ESTIMATED BUSINESS INCOME<br>YEAR ENDED 30 JUNE 2019</div>
  <div class="fig-currency">$</div>
  <table class="fig-table">
    <tr><td>Net Profit as per Interim Financials</td><td class="val">$330,020</td></tr>
    <tr class="blank"><td><span class="u">Add:</span> Allowance for Revenue (April - June)</td><td class="val rule">$280,000</td></tr>
    <tr><td></td><td class="val">$610,020</td></tr>
    <tr class="blank"><td><span class="u">Less:</span> Allowance for Expenses (April - June)</td><td class="val">$150,020</td></tr>
    <tr><td class="u">Estimated Net Income from Business</td><td class="val rule">$460,000</td></tr>
    <tr class="blank"><td></td><td class="val"></td></tr>
    <tr><td class="u">Less Proposed Tax Planning Strategies</td><td class="val"></td></tr>
    <tr class="blank"><td>Removal of Accounts Receivable</td><td class="val">$0</td></tr>
    <tr><td>Removal of Accounts Payable</td><td class="val">$0</td></tr>
    <tr class="blank"><td>Bring Forward Expenses</td><td class="val">$0</td></tr>
    <tr><td>Prepayment of Expenses</td><td class="val">$0</td></tr>
    <tr class="blank"><td>Defer Invoices</td><td class="val">$40,000</td></tr>
    <tr><td>Purchase of Equipment up to $30,000</td><td class="val">$30,000</td></tr>
    <tr class="blank"><td>One Year Lease</td><td class="val">$0</td></tr>
    <tr><td>Pay Employee Superannuation by 25th June 2019</td><td class="val">$2,000</td></tr>
    <tr class="blank"><td>Superannuation Contribution</td><td class="val">$0</td></tr>
    <tr><td class="u">Total Net Tax Planning Strategies</td><td class="val rule">$72,000</td></tr>
  </table>
  <div class="fig-total-top"></div>
  <div class="fig-total-row"><span>Estimated Taxable Income after Tax Planning Strategies</span><span class="num">$388,000</span></div>
  <div class="fig-total"></div>
  <footer class="page-foot">
    <svg width="360" height="16" viewBox="0 0 360 16" style="position:absolute;left:0;top:0"><rect width="360" height="16" fill="#6d6e71"/><polygon points="318,0 360,0 360,16 306,16" fill="#ffffff"/><polygon points="321,0 360,0 360,16 310,16" fill="#b5121b"/></svg>
    <span class="page-foot-copy">© 2020 HallettReeve Chartered Accountants</span>
    <span class="page-foot-num">4</span>
  </footer>
</section>

</body>
</html>
```